Photographer website

This website will contain information to sell the services of marvento quillas an up and coming photographer based in london
Updates

Target Market(s)

SME's for corporate head shots
mums for kids parties
actors - for headshots
up and coming models

Industry/Entity Type

Photographer

Number of Pages Required

3 page

Requirements
Must have
• Home
• About me
• Contact me
• Portfolio or gallery

```html
<!DOCTYPE html>
<html lang="en">
<head>
<meta charset="utf-8">
<title>Marvento Quillas Photography — Menu</title>
<link rel="stylesheet" href="https://fonts.googleapis.com/css2?family=Karla:wght@400;700&display=swap">
<style>
  :root {
    --bg: #232323;
    --text: #ffffff;
    --rule: #4a4a4a;
  }
  * { box-sizing: border-box; margin: 0; padding: 0; }
  html, body {
    width: 1200px;
    height: 574px;
    overflow: hidden;
    background: var(--bg);
  }
  .menu-overlay {
    position: relative;
    width: 1200px;
    height: 574px;
    background: var(--bg);
    color: var(--text);
    font-family: "Karla", sans-serif;
  }
  .main-nav {
    position: absolute;
    left: 100px;
    top: 46px;
    list-style: none;
  }
  .main-nav li { height: 46px; }
  .main-nav a {
    color: var(--text);
    text-decoration: none;
    font-size: 27px;
    font-weight: 400;
    letter-spacing: 0.3px;
    line-height: 40px;
    display: inline-block;
  }
  .main-nav a.is-active {
    border-bottom: 2px solid var(--text);
    line-height: 36px;
  }
  .close-button {
    position: absolute;
    left: 1086px;
    top: 52px;
    width: 18px;
    height: 18px;
  }
  .footer-rule {
    position: absolute;
    left: 87px;
    top: 492px;
    width: 1041px;
    height: 1px;
    background: var(--rule);
  }
  .copyright {
    position: absolute;
    left: 100px;
    top: 514px;
    font-size: 13px;
    font-weight: 700;
    letter-spacing: 0.1px;
  }
  .social-links {
    position: absolute;
    left: 967px;
    top: 515px;
    display: flex;
    gap: 9px;
    list-style: none;
  }
  .social-links li {
    width: 21px;
    height: 21px;
    border-radius: 50%;
    background: var(--text);
  }
</style>
</head>
<body>
  <div class="menu-overlay">
    <ul class="main-nav">
      <li><a href="#" class="is-active">Home</a></li>
      <li><a href="#">About Us</a></li>
      <li><a href="#">Portfolio</a></li>
      <li><a href="#">Contact</a></li>
    </ul>

    <svg class="close-button" viewBox="0 0 18 18" aria-label="Close menu">
      <line x1="1" y1="1" x2="17" y2="17" stroke="#ffffff" stroke-width="1.8"/>
      <line x1="17" y1="1" x2="1" y2="17" stroke="#ffffff" stroke-width="1.8"/>
    </svg>

    <div class="footer-rule"></div>
    <p class="copyright">© Copyright 2016. All Rights Reserved.</p>
    <ul class="social-links" aria-label="Social profiles">
      <li></li><li></li><li></li><li></li><li></li>
    </ul>
  </div>
</body>
</html>
```